Football blog needs a Wordpress design new site

We need a wordpress design for a new football blog site. We would like to see a design that uses the colours green, white and black and one that makes good use of the slideshow widgets as scene in the site 'www.tarnwick.net'
We would like a modern and sleek looking site but one that is also professional and easy to navigate.
Unfortunately due to unforeseen circumstances we are having to shorten the deadline date for this project.
The new deadline date is 16/07/2014.
We apologise for any inconveniance
Industry/Entity Type
It Professional
Look and feel

```html
<!DOCTYPE html>
<html lang="en">
<head>
<meta charset="utf-8">
<title>Sideline Chatter – Football Blog</title>
<link href="https://fonts.googleapis.com/css2?family=Open+Sans:wght@400;600;700&display=swap" rel="stylesheet">
<style>
:root{
  --green:#2f9e37;
  --green-dark:#24852c;
  --black:#0b0b0b;
  --ink:#333;
  --muted:#666;
  --line:#e3e3e3;
  --footer:#2b2b2b;
  --white:#fff;
}
*{box-sizing:border-box;margin:0;padding:0}
html,body{width:1200px;height:2223px;overflow:hidden;background:var(--white)}
body{position:relative;font-family:"Open Sans",Arial,sans-serif;color:var(--ink)}
.abs{position:absolute}
a{color:inherit;text-decoration:none}

/* top bar */
.topbar{left:0;top:0;width:1200px;height:45px;border-bottom:1px solid var(--line)}
.follow{position:absolute;left:770px;top:12px;font-size:13px;color:#444}
.social{position:absolute;top:5px;width:32px;height:32px;border-radius:50%}

/* header */
.header{left:0;top:45px;width:1200px;height:73px}
.brand{position:absolute;left:55px;top:12px;display:flex;align-items:center;gap:8px}
.brand-dot{width:46px;height:46px;border-radius:50%;background:var(--green)}
.brand-name{font-size:26px;font-weight:700;color:var(--green);letter-spacing:-.5px}
.nav{position:absolute;top:0;height:73px;font-size:14px;color:#222;line-height:73px}
.nav.active{color:var(--green);border-top:2px solid var(--green);line-height:69px}
.caret{display:inline-block;width:6px;height:6px;border-right:1px solid currentColor;border-bottom:1px solid currentColor;transform:rotate(45deg);margin:0 0 3px 6px}
.nav-divider{position:absolute;left:1085px;top:22px;width:1px;height:30px;background:var(--line)}

/* slider */
.slider{left:0;top:118px;width:1200px;height:379px;background:var(--black)}
.tile{position:absolute;overflow:hidden}
.caption{position:absolute;left:12px;bottom:12px;color:var(--white);font-weight:700;font-size:15px;white-space:nowrap}
.caption.big{font-size:26px;left:28px;bottom:28px}
.tag{display:inline-block;background:var(--green);color:var(--white);font-size:10px;font-weight:400;padding:3px 10px;margin:0 4px 6px 0;text-transform:uppercase}
.shade{position:absolute;left:0;right:0;bottom:0;height:60px;background:linear-gradient(transparent,rgba(0,0,0,.6))}

/* top stories */
.top-stories{left:0;top:497px;width:1200px;height:265px;background:var(--green)}
.top-stories h2{position:absolute;left:54px;top:15px;font-size:20px;font-weight:400;color:var(--white)}
.story{position:absolute;top:50px;width:328px;height:186px;overflow:hidden}
.story .bar{position:absolute;left:0;right:0;bottom:0;height:40px;background:rgba(0,0,0,.55)}
.story .tag{position:absolute;left:12px;bottom:44px;margin:0}
.story .title{position:absolute;left:12px;bottom:11px;color:var(--white);font-weight:700;font-size:15px}

/* latest news */
.section-title{font-size:20px;font-weight:400;color:#333;line-height:27px}
.post{position:absolute;left:54px;width:802px}
.post-img{position:absolute;left:0;top:0;width:246px;height:186px}
.post-body{position:absolute;left:276px;top:0;width:526px}
.post-title{font-size:20px;color:var(--green);font-weight:400;margin-top:0}
.meta{font-size:12px;color:#555;margin-top:12px;display:flex;gap:14px;align-items:center}
.meta i{display:inline-block;width:10px;height:10px;background:var(--green);margin-right:5px;vertical-align:-1px;border-radius:2px}
.excerpt{font-size:11.5px;line-height:16px;color:#555;margin-top:12px}
.more{display:block;font-size:12px;color:var(--green);margin-top:12px}
.rule{position:absolute;left:54px;width:802px;height:1px;background:var(--line)}

.pager{left:415px;top:1851px;display:flex;border:1px solid var(--line)}
.pager span{font-size:12px;color:var(--green);padding:0 12px;line-height:28px;border-left:1px solid var(--line)}
.pager span:first-child{border-left:0}
.pager .current{background:#eee;color:#333}

/* sidebar */
.side{left:883px;width:249px}
.editor{position:absolute;left:0;display:flex;gap:14px}
.avatar{width:38px;height:38px;flex:none}
.editor b{display:block;font-weight:400;font-size:14px;color:var(--green)}
.editor p{font-size:11.5px;line-height:16px;color:#555;width:170px}
.player{position:absolute;width:45px;height:47px}
.cat{position:absolute;left:0;width:249px;font-size:11.5px;color:#333;padding-left:15px;line-height:36px;border-bottom:1px solid var(--line)}
.cat::before{content:"";position:absolute;left:2px;top:15px;width:5px;height:5px;border-right:1px solid #333;border-top:1px solid #333;transform:rotate(45deg)}
.cat.on{color:var(--green)}
.tabs{position:absolute;left:0;top:38px;width:249px;height:30px;border-bottom:2px solid var(--green);display:flex}
.tab{font-size:12px;line-height:28px;padding:0 16px;background:#eee;color:#777;margin-right:4px}
.tab.on{background:var(--green);color:var(--white)}
.talk{position:absolute;left:14px;top:88px;width:225px;font-size:11.5px;line-height:16px;color:#444}
.tagpill{position:absolute;font-size:11.5px;color:#333;background:#eee;height:22px;line-height:22px;padding:0 14px 0 22px;white-space:nowrap}
.tagpill::before{content:"";position:absolute;left:8px;top:7px;width:8px;height:8px;background:var(--green);border-radius:1px}
.tagpill.on{background:var(--green);color:var(--white)}
.tagpill.on::before{background:var(--white)}

/* footer */
.footer{left:0;top:1964px;width:1200px;height:214px;background:var(--footer);color:#eee}
.footer h3{position:absolute;top:36px;font-size:19px;font-weight:400;color:var(--white)}
.foot-logo{position:absolute;left:54px;top:70px;width:84px;height:84px;background:var(--white);display:flex;flex-direction:column;align-items:center;justify-content:center;gap:4px}
.foot-logo .brand-dot{width:36px;height:36px}
.foot-logo span{font-size:10px;font-weight:700;color:var(--green)}
.foot-text{position:absolute;font-size:11.5px;line-height:17px;color:#ddd}
.subscribe{position:absolute;left:421px;top:112px;display:flex}
.subscribe .field{width:204px;height:30px;background:var(--white);color:#333;font-size:12px;line-height:30px;padding-left:10px}
.subscribe .btn{width:96px;height:30px;background:var(--green);color:var(--white);font-size:12px;font-weight:600;line-height:30px;text-align:center}
.tweet{position:absolute;left:790px;width:360px;padding-left:28px;font-size:11.5px;line-height:17px;color:#eee}
.tweet::before{content:"";position:absolute;left:0;top:3px;width:14px;height:14px;background:var(--white);border-radius:50%}
.tweet a{color:#6cc070}
.tweet em{font-style:normal;color:#999}

.bottombar{left:0;top:2178px;width:1200px;height:45px;background:var(--green);color:var(--white);font-size:11.5px;line-height:45px}
.bottombar .copy{position:absolute;left:54px}
.foot-icon{position:absolute;top:16px;width:13px;height:13px;border-radius:50%;background:var(--white)}
</style>
</head>
<body>

<header class="abs topbar">
  <span class="follow">Follow us!</span>
  <span class="social" style="left:851px;background:#3b5ea8"></span>
  <span class="social" style="left:895px;background:#2aa4dc"></span>
  <span class="social" style="left:939px;background:#1a75b3"></span>
  <span class="social" style="left:983px;background:#f0731f"></span>
  <span class="social" style="left:1027px;background:#d9442f"></span>
  <span class="social" style="left:1071px;background:#c8232c"></span>
</header>

<nav class="abs header">
  <div class="brand"><span class="brand-dot"></span><span class="brand-name">Sideline Chatter</span></div>
  <span class="nav" style="left:517px">Home</span>
  <span class="nav" style="left:600px">World Cup</span>
  <span class="nav" style="left:704px">Teams<span class="caret"></span></span>
  <span class="nav" style="left:793px">Standings<span class="caret"></span></span>
  <span class="nav active" style="left:882px;padding:0 16px">Blog<span class="caret"></span></span>
  <span class="nav" style="left:973px">Subscribe</span>
  <span class="nav-divider"></span>
  <svg class="abs" style="left:1100px;top:32px" width="16" height="16" viewBox="0 0 16 16"><circle cx="6.5" cy="6.5" r="5" fill="none" stroke="#999" stroke-width="1.6"/><line x1="10.2" y1="10.2" x2="14.5" y2="14.5" stroke="#999" stroke-width="1.8"/></svg>
</nav>

<section class="abs slider">
  <div class="tile" style="left:0;top:20px;width:100px;height:160px;background:linear-gradient(135deg,#c9a58a,#7c6a60)" role="img" aria-label="Player celebrating in white kit">
    <div class="shade"></div><div class="caption" style="left:-28px">Corrupti quos dolores etquas</div></div>
  <div class="tile" style="left:0;top:197px;width:100px;height:160px;background:linear-gradient(135deg,#d9732f,#6c4a3a)" role="img" aria-label="Player in orange kit">
    <div class="shade"></div><div class="caption" style="left:-28px">Corrupti quos dolores etquas</div></div>
  <div class="tile" style="left:116px;top:20px;width:229px;height:338px;background:linear-gradient(160deg,#e6cf4a,#3f8f3a 70%,#2d5a2a)" role="img" aria-label="Players in yellow kits celebrating on the pitch">
    <div class="shade"></div><div class="caption"><span class="tag">Sample tag</span><br>Corrupti quos dolores etquas</div></div>
  <div class="tile" style="left:361px;top:20px;width:461px;height:338px;background:linear-gradient(150deg,#5e5a52,#bfb8ad 45%,#3f5340)" role="img" aria-label="Two players in white kits celebrating a goal">
    <div class="shade" style="height:110px"></div><div class="caption big"><span class="tag">Germany</span><span class="tag">World Cup</span><br>Corrupti quos dolores etquas</div></div>
  <div class="tile" style="left:837px;top:20px;width:229px;height:160px;background:linear-gradient(150deg,#d6c13c,#4b8b3b)" role="img" aria-label="Fans cheering in the stands">
    <div class="shade"></div><div class="caption"><span class="tag">Sample tag</span><br>Corrupti quos dolores etquas</div></div>
  <div class="tile" style="left:837px;top:197px;width:229px;height:160px;background:linear-gradient(150deg,#e0b35a,#b88a4a)" role="img" aria-label="Supporter in sunglasses">
    <div class="shade"></div><div class="caption"><span class="tag">Sample tag</span><br>Corrupti quos dolores etquas</div></div>
  <div class="tile" style="left:1081px;top:20px;width:119px;height:160px;background:linear-gradient(150deg,#c93b33,#7a2a26)" role="img" aria-label="Player in red kit shouting">
  </div>
  <div class="tile" style="left:1081px;top:197px;width:119px;height:160px;background:linear-gradient(150deg,#c93b33,#3d7a3a)" role="img" aria-label="Player in red kit">
    <div class="shade"></div><div class="caption"><span class="tag">Sample tag</span><br>Corrupti quos</div></div>
</section>

<section class="abs top-stories">
  <h2>Top Stories</h2>
  <div class="story" style="left:54px;background:linear-gradient(150deg,#6b7b86,#b33a34 60%,#4a2a28)" role="img" aria-label="Team in red kits lined up">
    <div class="bar"></div><span class="tag">Sample tag</span><span class="title">Corrupti quos dolores etquas</span></div>
  <div class="story" style="left:409px;background:linear-gradient(150deg,#3f8a3f,#d6c27a 50%,#c0392b)" role="img" aria-label="Fan holding a flag">
    <div class="bar"></div><span class="tag">Sample tag</span><span class="title">Corrupti quos dolores etquas</span></div>
  <div class="story" style="left:767px;background:linear-gradient(150deg,#4d7a48,#d8d8d8 40%,#b8352e)" role="img" aria-label="Two players contesting the ball">
    <div class="bar"></div><span class="tag">Sample tag</span><span class="title">Corrupti quos dolores etquas</span></div>
</section>

<main>
  <h2 class="abs section-title" style="left:54px;top:790px">Latest News</h2>

  <article class="post" style="top:833px">
    <div class="post-img" style="background:linear-gradient(150deg,#d97a3a,#2f4e8c 60%,#4d8a3a)" role="img" aria-label="Player diving to celebrate"></div>
    <div class="post-body">
      <h3 class="post-title">Corrupti quos dolores etquas</h3>
      <div class="meta"><span><i></i>25/07/2013</span><span><i></i>17</span><span><i></i>Football, Worldcup, Standings</span></div>
      <p class="excerpt">At vero eos et accusamus et iusto odio dignissimos ducimus qui sint blanditiis prae sentium voluptatum deleniti atque corrupti quos dolores et quas molestias excepturi sint occaecati cupidi-tate non eleifend enim a feugiat. Pellentesque viverra vehicula sem ut volutpat. Lorem ipsum dolor sit amet, consectetur adipiscing condimentum eleifend enim a feugiat.</p>
      <a class="more">Read more ›</a>
    </div>
  </article>
  <div class="rule" style="top:1053px"></div>

  <article class="post" style="top:1096px">
    <div class="post-img" style="background:linear-gradient(150deg,#8cb8e0,#3a6fb0 60%,#d9d2c0)" role="img" aria-label="Fans with painted faces"></div>
    <div class="post-body">
      <h3 class="post-title">Corrupti quos dolores etquas</h3>
      <div class="meta"><span><i></i>25/07/2013</span><span><i></i>17</span><span><i></i>Football, Worldcup, Standings</span></div>
      <p class="excerpt">At vero eos et accusamus et iusto odio dignissimos ducimus qui sint blanditiis prae sentium voluptatum deleniti atque corrupti quos dolores et quas molestias excepturi sint occaecati cupidi-tate non eleifend enim a feugiat. Pellentesque viverra vehicula sem ut volutpat. Lorem ipsum dolor sit amet, consectetur adipiscing condimentum eleifend enim a feugiat.</p>
      <a class="more">Read more ›</a>
    </div>
  </article>
  <div class="rule" style="top:1315px"></div>

  <article class="post" style="top:1358px">
    <div class="post-img" style="background:linear-gradient(150deg,#3d7a3a,#d8c24a 50%,#9a9a92)" role="img" aria-label="Team celebrating together"></div>
    <div class="post-body">
      <h3 class="post-title">Corrupti quos dolores etquas</h3>
      <div class="meta"><span><i></i>25/07/2013</span><span><i></i>17</span><span><i></i>Football, Worldcup, Standings</span></div>
      <p class="excerpt">At vero eos et accusamus et iusto odio dignissimos ducimus qui sint blanditiis prae sentium voluptatum deleniti atque corrupti quos dolores et quas molestias excepturi sint occaecati cupidi-tate non eleifend enim a feugiat. Pellentesque viverra vehicula sem ut volutpat. Lorem ipsum dolor sit amet, consectetur adipiscing condimentum eleifend enim a feugiat.</p>
      <a class="more">Read more ›</a>
    </div>
  </article>
  <div class="rule" style="top:1578px"></div>

  <article class="post" style="top:1626px">
    <div class="post-img" style="background:linear-gradient(150deg,#c6322c,#e8c23a 50%,#2a2a2a)" role="img" aria-label="Cheering supporters"></div>
    <div class="post-body">
      <h3 class="post-title">Corrupti quos dolores etquas</h3>
      <div class="meta"><span><i></i>25/07/2013</span><span><i></i>17</span><span><i></i>Football, Worldcup, Standings</span></div>
      <p class="excerpt">At vero eos et accusamus et iusto odio dignissimos ducimus qui sint blanditiis prae sentium voluptatum deleniti atque corrupti quos dolores et quas molestias excepturi sint occaecati cupidi-tate non eleifend enim a feugiat. Pellentesque viverra vehicula sem ut volutpat. Lorem ipsum dolor sit amet.</p>
      <a class="more">Read more ›</a>
    </div>
  </article>

  <div class="abs pager"><span>Prev</span><span>1</span><span>2</span><span class="current">3</span><span>4</span><span>5</span><span>Next</span></div>
</main>

<aside>
  <div class="abs side" style="top:795px;height:250px">
    <h2 class="section-title">Editor’s Corner</h2>
    <div class="editor" style="top:43px"><span class="avatar" style="background:#c9a58a" role="img" aria-label="Editor portrait"></span><div><b>Letiusto gnissimos</b><p>Decusamus tiusto odiodig nis simos ducimus qui sint</p></div></div>
    <div class="editor" style="top:114px"><span class="avatar" style="background:#d8b89a" role="img" aria-label="Editor portrait"></span><div><b>Deiusto anissimos</b><p>Decusamus tiusto odiodig nis simos ducimus qui sint</p></div></div>
    <div class="editor" style="top:186px"><span class="avatar" style="background:#a07a62" role="img" aria-label="Editor portrait"></span><div><b>Tesiusto baissimos</b><p>Decusamus tiusto odiodig nis simos ducimus qui sint</p></div></div>
  </div>

  <div class="abs side" style="top:1046px;height:150px">
    <h2 class="section-title">Popular Football Players</h2>
    <span class="player" style="left:0;top:37px;background:#8a6d5a" role="img" aria-label="Player portrait"></span>
    <span class="player" style="left:58px;top:37px;background:#c8a48a" role="img" aria-label="Player portrait"></span>
    <span class="player" style="left:116px;top:37px;background:#6c6e6a;outline:2px solid #9fd4a2" role="img" aria-label="Player portrait"></span>
    <span class="player" style="left:174px;top:37px;background:#b08a72" role="img" aria-label="Player portrait"></span>
    <span class="player" style="left:0;top:96px;background:#7a5a48" role="img" aria-label="Player portrait"></span>
    <span class="player" style="left:58px;top:96px;background:#5a4a40" role="img" aria-label="Player portrait"></span>
    <span class="player" style="left:116px;top:96px;background:#8a7262" role="img" aria-label="Player portrait"></span>
    <span class="player" style="left:174px;top:96px;background:#c09a80" role="img" aria-label="Player portrait"></span>
  </div>

  <div class="abs side" style="top:1227px;height:230px">
    <h2 class="section-title">Categories</h2>
    <span class="cat" style="top:35px">Top Stories</span>
    <span class="cat" style="top:72px">Latest News (5)</span>
    <span class="cat on" style="top:109px">Euro Club League (12)</span>
    <span class="cat" style="top:146px">Players Updates (1)</span>
    <span class="cat" style="top:183px">World Cup Finals (3)</span>
  </div>

  <div class="abs side" style="top:1496px;height:200px">
    <h2 class="section-title">Popular Talks</h2>
    <div class="tabs"><span class="tab on">Multipurpose</span><span class="tab">Documented</span></div>
    <p class="talk">Raw denim you probably haven't heard of them jean shorts Austin. eu banh mi, qui irure dale ormsby ex squid Aliquip placeat salvia cillum handset.</p>
    <a class="abs more" style="left:14px;top:164px;margin:0">Read more ›</a>
  </div>

  <div class="abs side" style="top:1727px;height:130px">
    <h2 class="section-title">Tags</h2>
    <span class="tagpill" style="left:0;top:45px">Cup</span>
    <span class="tagpill" style="left:75px;top:45px">Worldcup</span>
    <span class="tagpill" style="left:160px;top:45px">NOR</span>
    <span class="tagpill" style="left:0;top:74px">Brazil</span>
    <span class="tagpill" style="left:94px;top:74px">ARG</span>
    <span class="tagpill" style="left:160px;top:74px">Ortez</span>
    <span class="tagpill on" style="left:0;top:103px">T. Varga</span>
    <span class="tagpill" style="left:116px;top:103px">Brandt</span>
  </div>
</aside>

<footer class="abs footer">
  <h3 style="left:54px">About</h3>
  <div class="foot-logo"><span class="brand-dot"></span><span>Sideline Chatter</span></div>
  <p class="foot-text" style="left:158px;top:70px;width:235px">Vivamus imperdiet felis consectetur onec eget orci adipiscing nunc. Pellen-tesque fermentum, ante ac interdum ullamcorper.</p>

  <h3 style="left:421px">Subscribe to our Newsletter</h3>
  <p class="foot-text" style="left:421px;top:70px;width:330px">Subscribe to our newsletter and stay up to date with the latest news and deals!</p>
  <div class="subscribe"><span class="field">youremail@mail.com</span><span class="btn">SUBSCRIBE</span></div>

  <h3 style="left:790px">Latest Tweets</h3>
  <p class="tweet" style="top:70px"><a>@fieldnotes</a> Imperdiet condimentum diam dolor lorem sit consectetur adipiscing <em>3 min ago</em></p>
  <p class="tweet" style="top:119px"><a>@fieldnotes</a> Sequat ipsum dolor onec eget orci fermentum condimentum lorem sit consectetur adipiscing <em>3 min ago</em></p>
</footer>

<div class="abs bottombar">
  <span class="copy">2014 © Sideline Chatter. ALL Rights Reserved. &nbsp;&nbsp; Privacy Policy | Terms of Service</span>
  <span class="foot-icon" style="left:901px"></span>
  <span class="foot-icon" style="left:924px"></span>
  <span class="foot-icon" style="left:947px"></span>
  <span class="foot-icon" style="left:970px"></span>
  <span class="foot-icon" style="left:993px"></span>
  <span class="foot-icon" style="left:1016px"></span>
  <span class="foot-icon" style="left:1039px"></span>
  <span class="foot-icon" style="left:1062px"></span>
  <span class="foot-icon" style="left:1085px"></span>
  <span class="foot-icon" style="left:1108px"></span>
</div>

</body>
</html>
```